Outdoor sign for Brindle Auto Restoration

I need a horizontal 4'x 8' outdoor roadside sign for my classic auto restoration business. I have uploaded colors and our logo. Needs the Brindle name, a prominent Classic AUTO RESTORATION, phone number and website. We rebuild and restore vintage cars, trucks and 4x4s. I'd like something clean but possibly retro. Classic Auto Restoration is more important than the Brindle name. It needs to be visible and readable from the street. NO CLIP ART

Target Market(s)

Customers who need their vintage care restored or upgraded. Men and women ages 25-75

Industry/Entity Type

Automotive

Colors
FFC000
F8CF3A
FAE287
FDF2CF
FEFAEE

Requirements
Must have
• Legible. Bright. Readable as a backlit 4' x 8' large horizontal sign (roughly 120cm X 240cm)
Nice to have
• Use of the Brindle logo/type, Complete or Classic before prominent AUTO RESTORATION
Should not have
• Clip art of old cars or icons. And we don't want the Brindle Logo from the website because it wont be legible from the road. I have included the Illustrator file for Brindle text in the uploads

```html
<!DOCTYPE html>
<html lang="en">
<head>
<meta charset="utf-8">
<title>Brindle Auto Restoration – Roadside Sign</title>
<link href="https://fonts.googleapis.com/css2?family=Anton&family=Oswald:wght@500&family=Pacifico&display=swap" rel="stylesheet">
<style>
  :root {
    --paper: #ffffff;
    --sign-black: #000000;
    --headline-grey: #e5e6e5;
    --amber: #f4ae03;
    --white: #ffffff;
  }
  html, body {
    margin: 0;
    padding: 0;
    width: 1200px;
    height: 600px;
    overflow: hidden;
    background: var(--paper);
  }
  .sign {
    display: block;
    width: 1200px;
    height: 600px;
  }
  .sign-panel { fill: var(--sign-black); }
  .rule { stroke: var(--amber); stroke-width: 4; }
  .headline-script {
    font-family: "Pacifico", cursive;
    fill: var(--white);
    font-size: 128px;
  }
  .headline-main {
    font-family: "Anton", sans-serif;
    fill: var(--headline-grey);
    font-size: 250px;
  }
  .business-name {
    font-family: "Anton", sans-serif;
    fill: var(--amber);
    font-size: 132px;
  }
  .contact {
    font-family: "Oswald", sans-serif;
    font-weight: 500;
    fill: var(--white);
    font-size: 78px;
  }
</style>
</head>
<body>
<svg class="sign" viewBox="0 0 2560 1280" xmlns="http://www.w3.org/2000/svg" role="img" aria-label="Classic Auto Restoration – Brindle roadside sign">
  <rect class="sign-panel" x="257" y="130" width="2063" height="1030"/>

  <!-- headline -->
  <text class="headline-script" x="1270" y="380" text-anchor="middle">Classic</text>
  <text class="headline-main" x="1270" y="720" text-anchor="middle" textLength="1670" lengthAdjust="spacingAndGlyphs">AUTO RESTORATION</text>

  <!-- contact strip -->
  <line class="rule" x1="342" y1="979" x2="931" y2="979"/>
  <line class="rule" x1="342" y1="1081" x2="931" y2="1081"/>
  <line class="rule" x1="1577" y1="979" x2="2224" y2="979"/>
  <line class="rule" x1="1577" y1="1081" x2="2224" y2="1081"/>

  <text class="contact" x="630" y="1055" text-anchor="middle" textLength="400" lengthAdjust="spacingAndGlyphs">555-214-7390</text>
  <text class="business-name" x="1253" y="1075" text-anchor="middle" textLength="575" lengthAdjust="spacingAndGlyphs">BRINDLE</text>
  <text class="contact" x="1898" y="1055" text-anchor="middle" textLength="615" lengthAdjust="spacingAndGlyphs">brindlerestorations.com</text>
</svg>
</body>
</html>
```